Graphic Banner Design - 2.5' x 6' - High Tech Company

We are in need of a banner design for an outdoor sign that will be used at sponsorship events.

Size
2.5' x 6'

The company is a high tech company, and the design will be used for action sports events. So lining up to that would be good.

Tag line to be incorporated...
"Extreme IT Services for Extreme Needs."

Target Market(s)

Business Owners, Entrepreneurs, IT Professionals.

Industry/Entity Type

Information Technology

Logo Text

Vexlora

Colors

Designer to choose colors to be used in the design.

Requirements
Must have
• Must feel young and vibrant, fit in to an action sports event and just be out of this world awesome.
• In the world of the IT, we are the Zanverolli. Fast, Awesome, not necessarily cheap, but you know it will do what you want extremely well. Not for everyone, but always desired.

```html
<!DOCTYPE html>
<html lang="en">
<head>
<meta charset="utf-8">
<title>Vexlora – Extreme IT Services Banner</title>
<link rel="stylesheet" href="https://fonts.googleapis.com/css2?family=Roboto:wght@700&family=Montserrat:wght@400&display=swap">
<style>
  :root {
    --brand-blue: #2f58ab;
    --brand-blue-deep: #182f66;
    --brand-blue-light: #5a86d4;
    --stage-glow: #a9c3f0;
    --mist: #d9dbe0;
    --mist-light: #f6f6f7;
    --white: #ffffff;
    --logo-blue: #3a62b4;
  }
  html, body {
    margin: 0;
    padding: 0;
    overflow: hidden;
    background: var(--white);
  }
  .banner {
    position: relative;
    width: 1200px;
    height: 500px;
    overflow: hidden;
    background: var(--mist-light);
  }
  .banner__art {
    position: absolute;
    inset: 0;
    width: 1200px;
    height: 500px;
  }
  .tagline {
    position: absolute;
    left: 72px;
    top: 98px;
    margin: 0;
    font-family: "Roboto", Arial, sans-serif;
    font-weight: 700;
    font-size: 64px;
    line-height: 84px;
    letter-spacing: 0.6px;
    text-transform: uppercase;
    color: var(--white);
    text-shadow: 0 2px 8px rgba(10, 25, 60, 0.45);
    white-space: nowrap;
  }
  .logo {
    position: absolute;
    left: 836px;
    top: 398px;
    margin: 0;
    font-family: "Montserrat", Arial, sans-serif;
    font-weight: 400;
    font-size: 36px;
    line-height: 44px;
    color: var(--logo-blue);
  }
</style>
</head>
<body>
  <div class="banner">
    <svg class="banner__art" viewBox="0 0 1200 500" xmlns="http://www.w3.org/2000/svg">
      <defs>
        <clipPath id="crowd-clip">
          <polygon points="0,0 882,0 984,96 670,500 0,500"/>
        </clipPath>
        <linearGradient id="crowd-base" x1="0" y1="0" x2="0" y2="1">
          <stop offset="0" stop-color="var(--brand-blue)"/>
          <stop offset="0.55" stop-color="#2a4f9c"/>
          <stop offset="1" stop-color="var(--brand-blue-deep)"/>
        </linearGradient>
        <radialGradient id="light-glow" cx="0.5" cy="0.5" r="0.5">
          <stop offset="0" stop-color="var(--stage-glow)" stop-opacity="0.75"/>
          <stop offset="1" stop-color="var(--stage-glow)" stop-opacity="0"/>
        </radialGradient>
        <linearGradient id="crowd-shade" x1="0" y1="0" x2="0" y2="1">
          <stop offset="0.45" stop-color="var(--brand-blue-deep)" stop-opacity="0"/>
          <stop offset="1" stop-color="var(--brand-blue-deep)" stop-opacity="0.8"/>
        </linearGradient>
        <linearGradient id="haze-base" x1="0" y1="0" x2="0" y2="1">
          <stop offset="0" stop-color="var(--mist-light)"/>
          <stop offset="1" stop-color="var(--mist)"/>
        </linearGradient>
        <radialGradient id="haze-glow" cx="0.5" cy="0.5" r="0.5">
          <stop offset="0" stop-color="var(--white)" stop-opacity="0.95"/>
          <stop offset="1" stop-color="var(--white)" stop-opacity="0"/>
        </radialGradient>
        <filter id="band-shadow" x="-10%" y="-10%" width="120%" height="120%">
          <feDropShadow dx="-4" dy="2" stdDeviation="6" flood-color="#0b1e48" flood-opacity="0.4"/>
        </filter>
      </defs>

      <g class="stage-backdrop" role="img" aria-label="Faded photo of a concert crowd with raised hands under bright stage lights">
        <rect width="1200" height="500" fill="url(#haze-base)"/>
        <ellipse cx="1150" cy="40" rx="160" ry="110" fill="url(#haze-glow)"/>
        <ellipse cx="960" cy="260" rx="220" ry="120" fill="url(#haze-glow)"/>
      </g>

      <g class="crowd-panel" clip-path="url(#crowd-clip)" role="img" aria-label="Blue-tinted photo of a cheering concert crowd with hands raised toward the stage lights">
        <rect width="1200" height="500" fill="url(#crowd-base)"/>
        <ellipse cx="270" cy="40" rx="200" ry="120" fill="url(#light-glow)"/>
        <ellipse cx="560" cy="70" rx="230" ry="140" fill="url(#light-glow)"/>
        <ellipse cx="800" cy="30" rx="170" ry="110" fill="url(#light-glow)"/>
        <ellipse cx="420" cy="230" rx="260" ry="70" fill="url(#light-glow)" opacity="0.5"/>
        <rect width="1200" height="500" fill="url(#crowd-shade)"/>
      </g>

      <polygon class="chevron-band" points="882,0 960,0 1072,96 760,500 670,500 984,96"
               fill="var(--white)" filter="url(#band-shadow)"/>
    </svg>

    <h1 class="tagline">Extreme IT Services<br>for Extreme Needs</h1>
    <p class="logo">Vexlora</p>
  </div>
</body>
</html>
```